New Web Design Project for kitchen company

We need a homepage mockup for a company that sells and installs kitchen and baths. Use your creative talent to come up with something visually appeal and professional for this web-site.

Please see the attached brief.

If you have any questions feel free to post them right on the project discussion.

Target Market(s)

homeowners

Number of Pages Required

1 page

Font styles to use
Serif
Other font styles liked:
• Something similar to the logo

```html
<!DOCTYPE html>
<html lang="en">
<head>
<meta charset="utf-8">
<title>Harborline Kitchen and Bath</title>
<link href="https://fonts.googleapis.com/css2?family=Open+Sans:wght@300;400;600&display=swap" rel="stylesheet">
<style>
:root{
  --page:#f7f7f7;
  --white:#ffffff;
  --ink:#333333;
  --muted:#555555;
  --nav:#333333;
  --footer:#3a3a3a;
  --quote:#b5b5b5;
  --rule:#444444;
}
*{margin:0;padding:0;box-sizing:border-box}
html,body{width:1200px;height:2996px;overflow:hidden}
body{background:var(--page);font-family:"Open Sans",Arial,sans-serif;color:var(--ink);position:relative}
.abs{position:absolute}
.center{left:0;width:1200px;text-align:center}

/* header */
.site-header{top:0;left:0;width:1200px;height:75px;background:var(--page)}
.brand{top:24px;left:0;width:1200px;display:flex;justify-content:center;align-items:center;gap:8px;font-size:14px;letter-spacing:1px;color:#222}
.brand-dot{width:26px;height:26px;border-radius:50%;background:#222}
.main-nav{top:75px;left:0;width:1200px;height:38px;background:var(--nav);display:flex;justify-content:center;gap:0}
.main-nav a{color:#e6e6e6;font-size:10.5px;letter-spacing:2px;text-decoration:none;line-height:38px;margin:0 20px;position:relative}
.main-nav a.active::after{content:"";position:absolute;left:0;right:0;bottom:2px;height:2px;background:#ddd}

/* hero */
.hero{top:113px;left:0;width:1200px;height:599px;
  background:linear-gradient(180deg,#050505 0%,#2b2d31 25%,#4b5058 55%,#585a5c 80%,#3d3a38 100%)}
.hero-title{top:42px;font-size:29px;font-weight:400;letter-spacing:1.5px;color:#fff}
.hero-sub{top:90px;font-size:17px;letter-spacing:1px;color:#fff}
.btn-outline{top:160px;left:529px;width:142px;height:37px;border:1px solid #fff;color:#fff;font-size:11px;letter-spacing:.5px;line-height:35px;text-align:center}

/* section headings */
.section-title{font-size:27px;font-weight:400;letter-spacing:1.5px}
.title-rule{left:580px;width:40px;height:1px;background:var(--rule)}

/* projects */
.projects{top:828px;left:150px;width:900px}
.project-row{position:relative;width:900px;height:300px;margin-bottom:38px;display:flex}
.photo{width:300px;height:300px}
.photo-bath{background:linear-gradient(135deg,#b9c1c4 0%,#e6e6e2 45%,#f4f3ef 60%,#7b6b5a 100%)}
.photo-kitchen-a{background:linear-gradient(160deg,#d9d8d2 0%,#f2f1ec 40%,#66625d 70%,#6a4630 100%)}
.photo-kitchen-b{background:linear-gradient(160deg,#e4e3de 0%,#f6f5f1 45%,#3e2a20 75%,#7a5a40 100%)}
.photo-kitchen-c{background:linear-gradient(160deg,#c6cbd2 0%,#e9ebee 40%,#7d8b9c 65%,#dfe0e2 100%)}
.project-mid{width:300px;height:300px;background:var(--page);position:relative}
.project-info{position:absolute;left:0;width:300px;height:100px;background:var(--white);font-size:13px;letter-spacing:1px;line-height:18px;color:#444;padding:14px 0 0 35px}
.info-top{top:0}
.info-bottom{bottom:0;padding-left:30px}
.info-top::before{content:"";position:absolute;left:-22px;top:34px;border-style:solid;border-width:22px 22px 22px 0;border-color:transparent var(--white) transparent transparent}
.info-bottom::after{content:"";position:absolute;right:-22px;top:34px;border-style:solid;border-width:22px 0 22px 22px;border-color:transparent transparent transparent var(--white)}

/* services */
.services{top:1518px;left:0;width:1200px;height:439px;
  background:linear-gradient(90deg,#c9ced5 0%,#e7eaee 30%,#eef0f3 55%,#c4ccd6 80%,#a9b1bb 100%)}
.body-copy{font-size:13.5px;letter-spacing:.6px;line-height:18px}
.btn-dark{top:354px;left:530px;width:140px;height:35px;background:#2c2c2c;border:1px solid #fff;color:#fff;font-size:11px;line-height:33px;text-align:center}

/* about */
.about{top:1957px;left:0;width:1200px;height:439px;
  background:linear-gradient(180deg,#4d4e50 0%,#606264 40%,#55585b 70%,#6a6c6d 100%);color:#fff}

/* testimonials */
.testimonials{top:2396px;left:0;width:1200px;height:375px;background:var(--page)}
.quote-mark{font-family:Georgia,serif;font-size:130px;color:var(--quote);line-height:1}
.quote-text{top:134px;left:290px;width:620px;text-align:center;font-size:13.5px;line-height:18px;color:#444}
.author{top:265px;font-size:17px;color:#666}
.dots{top:300px;left:578px;display:flex;gap:7px}
.dot{width:10px;height:10px;border-radius:50%;border:1px solid #444}
.dot.on{background:#333}

/* footer */
.site-footer{top:2771px;left:0;width:1200px;height:225px;background:var(--footer);color:#e6e6e6;font-size:10px;line-height:12.5px}
.footer-brand{top:107px;left:934px;display:flex;align-items:center;gap:6px;font-size:13px;color:#fff}
.footer-brand .brand-dot{width:22px;height:22px;background:#fff}
</style>
</head>
<body>

<header class="abs site-header">
  <div class="abs brand"><span class="brand-dot"></span>HARBORLINE KITCHEN AND BATH</div>
</header>
<nav class="abs main-nav">
  <a class="active">HOME</a><a>ABOUT US</a><a>GALLERY</a><a>OUR PROJECTS</a><a>SEVRICES</a><a>CONTACT US</a>
</nav>

<section class="abs hero" role="img" aria-label="Photo of a remodeled grey and white kitchen with island and stools">
  <h1 class="abs center hero-title">Welcome to Harborline Kitchen and Bath</h1>
  <p class="abs center hero-sub">COMITED TO QUALITY</p>
  <div class="abs btn-outline">EXPLORE OUR WORK</div>
</section>

<h2 class="abs center section-title" style="top:752px">RECENT PROJECTS</h2>
<div class="abs title-rule" style="top:803px"></div>

<div class="abs projects">
  <div class="project-row">
    <div class="photo photo-bath" role="img" aria-label="Bathroom with freestanding white tub under windows"></div>
    <div class="project-mid">
      <div class="project-info info-top">MARK AND DIANE'S BATHROOM<br>TRANSITIONAL, BOSTON<br>PROJECT YEAR: 2018<br>PROJECT COST: $50,001 - $75,000</div>
      <div class="project-info info-bottom">OWEN AND CLARA'S KITCHEN<br>BOSTON<br>PROJECT YEAR: 2018<br>PROJECT COST: $???,??? - ???,???</div>
    </div>
    <div class="photo photo-kitchen-a" role="img" aria-label="White kitchen with grey island and dark stools"></div>
  </div>
  <div class="project-row">
    <div class="photo photo-kitchen-b" role="img" aria-label="White kitchen with dark countertop island and pendant lights"></div>
    <div class="project-mid">
      <div class="project-info info-top">HADLEY'S KITCHEN<br>TRADITIONAL, BOSTON<br>PROJECT YEAR: 2014<br>PROJECT COST: $???,??? - $???,???</div>
      <div class="project-info info-bottom">CARVER KITCHEN REMODEL<br>TRANSITIONAL KITCHEN, BOSTON<br>PROJECT YEAR: 2018<br>PROJECT COST: $???,??? - ???,???</div>
    </div>
    <div class="photo photo-kitchen-c" role="img" aria-label="Bright kitchen with blue tile backsplash and marble counter"></div>
  </div>
</div>

<section class="abs services" role="img" aria-label="Blurred kitchen background photo">
  <h2 class="abs center section-title" style="top:40px">SERVICES</h2>
  <div class="abs title-rule" style="top:93px"></div>
  <p class="abs center body-copy" style="top:113px">At Harborline Kitchen and Bath, we are a full-service kitchen and bath design, sales, and<br>installation firm. With over 35 years of industry experience, Harborline has become the #1<br>most recommended kitchen and bath remodeling company in the Metro-West and Greater Boston area.</p>
  <p class="abs center body-copy" style="top:184px">We can manage your entire remodeling project from start to finish; or work with your contractor<br>to design and assist in installation of your kitchen or bath.</p>
  <p class="abs center body-copy" style="top:238px">We take great pride in our work and our happy clients!</p>
  <p class="abs center body-copy" style="top:326px">Schedule Your In-Home Consultation Today!</p>
  <div class="abs btn-dark">REQUEST A QUOTE</div>
</section>

<section class="abs about" role="img" aria-label="Blurred dark kitchen background photo">
  <h2 class="abs center section-title" style="top:40px">ABOUT US</h2>
  <div class="abs title-rule" style="top:93px;background:#ddd"></div>
  <p class="abs center body-copy" style="top:114px">Our 30th Year in the Kitchen and Bath Industry!</p>
  <p class="abs center body-copy" style="top:150px">In 1989, Tom and Ellen Varga started Harborline Kitchens out of a small storefront in Westbrook,<br>MA. In order to find more room for their growing business, they moved their showroom to its<br>current location in Ashfield, MA. 30 years and thousands of happy clients later, Harborline Kitchen<br>and Bath is still committed to exceptional quality of work and design.</p>
  <p class="abs center body-copy" style="top:240px">In early 2019, Tom Ashby was brought on to continue the rich tradition of Harborline and work<br>along Tom Varga. Both Tom's are looking forward to the next chapter in Harborline!</p>
</section>

<section class="abs testimonials">
  <h2 class="abs center section-title" style="top:40px">TESTIMONIALS</h2>
  <div class="abs title-rule" style="top:93px"></div>
  <div class="abs quote-mark" style="top:112px;left:210px">&ldquo;</div>
  <p class="abs quote-text">"I recently had the pleasure of working with Tom Varga of Harborline Kitchens on my kitchen and dining room renovation. Tom was instrumental in carrying out this project from design to completion. He has an excellent crew of craftsmen that are professional, talented,<br>and leave the worksite clean every day. Tom was responsive to any issues that came up and took care of them quickly and efficiently. My kitchen and dining room were completed on time and are beautiful!"</p>
  <div class="abs quote-mark" style="top:172px;left:918px">&rdquo;</div>
  <p class="abs center author">~Rita~</p>
  <svg class="abs" style="top:292px;left:476px" width="18" height="30" viewBox="0 0 18 30"><polyline points="15,2 3,15 15,28" fill="none" stroke="#333" stroke-width="2"/></svg>
  <div class="abs dots"><span class="dot on"></span><span class="dot"></span><span class="dot"></span></div>
  <svg class="abs" style="top:292px;left:706px" width="18" height="30" viewBox="0 0 18 30"><polyline points="3,2 15,15 3,28" fill="none" stroke="#333" stroke-width="2"/></svg>
</section>

<footer class="abs site-footer">
  <p class="abs" style="top:50px;left:151px">Contacts:</p>
  <p class="abs" style="top:75px;left:151px">Ashfield Showroom<br>118 Orchard Lane<br>Ashfield, MA<br>555-014-2290<br>tom@harborlinekb.com</p>
  <p class="abs" style="top:75px;left:279px">Home<br>About Us<br>Gallery<br>Our Projects<br>Services</p>
  <div class="abs footer-brand"><span class="brand-dot"></span>HARBORLINE</div>
  <p class="abs center" style="top:167px;font-size:9px">Copyright 2020 Harborline Kitchen and Bath Inc.</p>
</footer>

</body>
</html>
```